For Lease Sign to Attract National Retail Tenants

Attached is a logo design that was created by Pixel Harbor. I will like to develop a leasing sign that is 4 foot wide by 4 foot high or 4 feet wide and 6 feet high. I would like the sign to have a black background and use the colors that are in the logo. These will be signs that are placed in front of shopping centers and are often read by passing motorist so the sign must be simple, clean, very easy to read, distinctive, and have as few words as possible. It would be good if small amounts of bright green can be added as a boarder or ????? The text should be FOR LEASE, 555-283-7716, Wade Hollins. I will want to also design cards and letter head around the same theme.

Target Market(s)

National retail tenants wanting to lease space in my shopping centers

Industry/Entity Type

Real Estate Development

Contact Information for Business Card

Tern Holdings KR, LLC Wade Hollins President & CEO 4127 Orvell Ave. Suite 308 La Jolla, CA 92037 555-283-7716 wadehollins@mailvexa.example

```html
<!DOCTYPE html>
<html lang="en">
<head>
<meta charset="utf-8">
<title>For Lease Signs – Tern Holdings KR, LLC</title>
<link rel="stylesheet" href="https://fonts.googleapis.com/css2?family=Montserrat:wght@600;700&family=Oswald:wght@500;600&display=swap">
<style>
  :root {
    --sign-black: #231f20;
    --accent-green: #3dbb1c;
    --text-white: #ffffff;
    --brand-grey: #c9cacc;
    --brand-red: #e3111b;
    --page-bg: #ffffff;
  }
  * { margin: 0; padding: 0; box-sizing: border-box; }
  html, body {
    width: 1200px;
    height: 720px;
    overflow: hidden;
    background: var(--page-bg);
  }
  .canvas {
    position: relative;
    width: 1200px;
    height: 720px;
  }
  .sign {
    position: absolute;
    background: var(--sign-black);
    border-top: 10px solid var(--accent-green);
    color: var(--text-white);
    text-align: center;
    overflow: hidden;
  }
  .sign--square { left: 135px; top: 266px; width: 381px; height: 379px; }
  .sign--tall   { left: 683px; top: 76px;  width: 380px; height: 569px; }

  .sign__headline,
  .sign__phone {
    position: absolute;
    left: 0;
    right: 0;
    line-height: 1;
    white-space: nowrap;
  }
  .sign--square .sign__headline {
    top: 28px;
    font: 700 55px/1 "Montserrat", sans-serif;
  }
  .sign--square .sign__phone {
    top: 93px;
    font: 700 47px/1 "Montserrat", sans-serif;
  }
  .sign--tall .sign__headline {
    top: 46px;
    font: 600 78px/1 "Oswald", sans-serif;
    transform: scaleY(1.08);
    transform-origin: center top;
  }
  .sign--tall .sign__phone {
    top: 150px;
    font: 600 57px/1 "Oswald", sans-serif;
  }

  .sign__contact {
    position: absolute;
    left: 0;
    right: 0;
    display: flex;
    align-items: center;
    gap: 20px;
  }
  .sign__contact::before,
  .sign__contact::after {
    content: "";
    flex: 1;
    height: 6px;
    background: var(--accent-green);
  }
  .sign__contact-name {
    font: 700 21px/1 "Montserrat", sans-serif;
    letter-spacing: 0.3px;
    white-space: nowrap;
  }
  .sign--square .sign__contact { top: 169px; }
  .sign--tall .sign__contact   { top: 265px; }
  .sign--tall .sign__contact-name { font-size: 22px; }

  .brand {
    position: absolute;
    left: 0;
    right: 0;
    display: flex;
    justify-content: center;
    align-items: center;
    gap: 10px;
  }
  .brand__mark {
    background: var(--brand-red);
    flex: none;
  }
  .brand__name {
    font-family: "Montserrat", sans-serif;
    font-weight: 600;
    color: var(--brand-grey);
    letter-spacing: 0.5px;
    white-space: nowrap;
  }
  .sign--square .brand { top: 300px; }
  .sign--square .brand__mark { width: 14px; height: 14px; }
  .sign--square .brand__name { font-size: 17px; }
  .sign--tall .brand { top: 462px; }
  .sign--tall .brand__mark { width: 18px; height: 18px; }
  .sign--tall .brand__name { font-size: 22px; }
</style>
</head>
<body>
<main class="canvas">

  <section class="sign sign--square" aria-label="For lease sign, 4 by 4 feet">
    <h1 class="sign__headline">FOR LEASE</h1>
    <p class="sign__phone">555-283-7716</p>
    <div class="sign__contact"><span class="sign__contact-name">WADE HOLLINS</span></div>
    <div class="brand">
      <span class="brand__mark" aria-hidden="true"></span>
      <span class="brand__name">TERN HOLDINGS KR, LLC</span>
    </div>
  </section>

  <section class="sign sign--tall" aria-label="For lease sign, 4 by 6 feet">
    <h1 class="sign__headline">FOR LEASE</h1>
    <p class="sign__phone">555-283-7716</p>
    <div class="sign__contact"><span class="sign__contact-name">WADE HOLLINS</span></div>
    <div class="brand">
      <span class="brand__mark" aria-hidden="true"></span>
      <span class="brand__name">TERN HOLDINGS KR, LLC</span>
    </div>
  </section>

</main>
</body>
</html>
```